Landing page in the senior sector

We need a landing page for families looking for retirement homes for their parent. The target is rather old (50-60 years old). The mandatory fields are Name, Email, Phone. The optional fields are budget, research zipcode, Emergency (,,). It is important to note that this is a free service that we offer to families in research. It should be noted that they are often in distress and repulsive. Need a mobile landing We need a landing page to recruit families looking for retirement homes for their parent. The target is rather old (50-60 years old). Required fields are Name, Email, Phone. The optional fields (they may not appear at all) are Budget, Search CP, Emergency (,,). It is important to mention that this is a free service that we offer to families in search. It should be noted that they are often in distress and that asking them for input may let tel may seem repulsive. Also need a mobile version

Target Market(s)

rather old (50-60 years old) / rather old (50-60 years old)

Coding

Coded - Design and coding required

Number of Pages Required

2 page

Font styles to use
Sans Serif

Colors

Designer to choose colors to be used in the design.

Requirements
Must have
• - A form with the 3 mandatory fields / A form with the 3 mandatory fields - Optimized for conversion / Optimized for conversion

```html
<!DOCTYPE html>
<html lang="en">
<head>
<meta charset="UTF-8">
<title>Golden Haven Care – Free Retirement Home Search</title>
<link href="https://fonts.googleapis.com/css2?family=Kurale&family=Nunito+Sans:wght@400;600;700&display=swap" rel="stylesheet">
<style>
  :root {
    --panel-green: #8db21a;
    --panel-green-light: #9cc02a;
    --white: #ffffff;
    --button-blue: #0a72c9;
    --photo-sky: #c9d3c0;
    --photo-house: #d8d1c4;
    --photo-lawn: #7f9a4a;
  }
  * { box-sizing: border-box; margin: 0; padding: 0; }
  html, body { width: 1200px; height: 857px; overflow: hidden; }
  body { font-family: "Nunito Sans", sans-serif; color: var(--white); }

  .landing {
    position: relative;
    width: 1200px;
    height: 857px;
    overflow: hidden;
  }
  .hero-photo {
    position: absolute;
    inset: 0;
    background:
      linear-gradient(180deg, rgba(0,0,0,0) 60%, rgba(70,90,40,0.35) 100%),
      radial-gradient(ellipse at 55% 35%, var(--photo-house) 0%, rgba(216,209,196,0) 45%),
      radial-gradient(ellipse at 30% 80%, #e3e3e6 0%, rgba(227,227,230,0) 40%),
      linear-gradient(180deg, var(--photo-sky) 0%, #b7c29b 45%, var(--photo-lawn) 100%);
  }
  .panel-shape {
    position: absolute;
    inset: 0;
    width: 1200px;
    height: 857px;
  }

  .brand {
    position: absolute;
    left: 110px;
    top: 116px;
    width: 176px;
    text-align: center;
    font-family: "Nunito Sans", sans-serif;
    font-weight: 700;
    font-size: 21px;
    letter-spacing: 0.5px;
    color: var(--white);
    text-transform: uppercase;
  }

  .headline {
    position: absolute;
    right: 120px;
    top: 64px;
    text-align: right;
    font-family: "Kurale", serif;
    font-size: 34px;
    line-height: 50px;
    color: var(--white);
  }
  .headline .upper { text-transform: uppercase; display: block; }
  .headline .mixed { display: block; }

  .lead-form {
    position: absolute;
    left: 703px;
    top: 334px;
    width: 377px;
    display: grid;
    grid-template-columns: 183px 183px;
    column-gap: 11px;
    row-gap: 9px;
  }
  .lead-form input {
    height: 43px;
    border: 2px solid var(--white);
    background: rgba(255,255,255,0.08);
    color: var(--white);
    font-family: "Nunito Sans", sans-serif;
    font-size: 16px;
    padding: 0 10px;
    outline: none;
  }
  .lead-form input::placeholder { color: var(--white); opacity: 1; }
  .lead-form .field-wide { grid-column: 1 / 3; }
  .lead-form .submit-button {
    grid-column: 2 / 3;
    justify-self: end;
    margin-top: 8px;
    width: 107px;
    height: 43px;
    border: 2px solid var(--white);
    background: var(--button-blue);
    color: var(--white);
    font-family: "Nunito Sans", sans-serif;
    font-size: 17px;
    cursor: pointer;
  }

  .footer-note {
    position: absolute;
    right: 120px;
    top: 785px;
    text-align: right;
    font-size: 17px;
    line-height: 26px;
    color: var(--white);
  }
</style>
</head>
<body>
<main class="landing">
  <div class="hero-photo" role="img" aria-label="Photo of an elderly couple seen from behind, arm in arm, looking at a house surrounded by trees"></div>

  <svg class="panel-shape" viewBox="0 0 1200 857" aria-hidden="true">
    <path d="M806 0 C 650 200, 600 560, 849 857 L1200 857 L1200 0 Z" fill="var(--panel-green)"/>
    <path d="M806 0 C 650 200, 600 560, 849 857" fill="none" stroke="var(--white)" stroke-width="4"/>
  </svg>

  <div class="brand">Golden Haven Care</div>

  <h1 class="headline">
    <span class="upper">We offer free</span>
    <span class="upper">service</span>
    <span class="mixed">Retirement Homes</span>
    <span class="upper">for your parents</span>
  </h1>

  <form class="lead-form">
    <input type="text" name="name" placeholder="Name" required>
    <input type="email" name="email" placeholder="Email" required>
    <input type="tel" name="phone" placeholder="Phone" required>
    <input type="text" name="budget" placeholder="Budget">
    <input type="text" name="search-cp" placeholder="Search CP">
    <input type="text" name="zipcode" placeholder="Zipcode">
    <input class="field-wide" type="text" name="emergency" placeholder="Emergency">
    <button class="submit-button" type="submit">Submit</button>
  </form>

  <p class="footer-note">Copyrights @ 2018 Golden Haven<br>Care. All Rights Reserved.</p>
</main>
</body>
</html>
```